New Business Card Design Project VORALDI-Italy

we are VORALDI-Italy
our company in the market for 3 years we are luxury cosmetic company and its about time for a facelift :)
i will like to have elegant luxurious and unique business card
that will give the person that get it a unique, luxurious and elegant impression
I'm VERY OPEN FOR NEW IDEAS , even duo i add a few files of things that i see on line and i like them

i add my logo as well
my website is VORALDI.COM
(if you would like to see the main style that we have)

Target Market(s)

adult that have money :)

Industry/Entity Type

Business

Contact Information for Business Card

Name - Paul Voraldi
Position - CEO and CO Founder
address - 4718 E Danbury
telephone - 555-318-4402
email - paul@voraldi-example.com
fax - 555-318-4402
website - VORALDI.COM

Colors
000000
959595
fbee3e
ffffff

Requirements
Must have
• big logo in GOLD color
• elegant look
• impressive
Nice to have
• not must but maybe classy pattern background
• not must but maybe emblem
• maybe clear plastic business card
Should not have
• colors
• images

```html
<!DOCTYPE html>
<html lang="en">
<head>
<meta charset="utf-8">
<title>VORALDI-Italy — Business Card</title>
<link href="https://fonts.googleapis.com/css2?family=Cinzel:wght@400;600;700&family=Montserrat:wght@400;500&display=swap" rel="stylesheet">
<style>
  :root {
    --canvas: #e9e7e3;
    --card-dark: #2a2420;
    --card-dark-deep: #1f1a17;
    --gold: #d6b25a;
    --gold-light: #ecd48d;
    --gold-deep: #a9823a;
    --ink: #231e1b;
    --text-light: #e8d9ab;
  }
  * { margin: 0; padding: 0; box-sizing: border-box; }
  html, body { width: 848px; height: 1200px; overflow: hidden; }
  body {
    background: var(--canvas);
    display: flex;
    align-items: center;
    justify-content: center;
    gap: 44px;
  }
  .card {
    position: relative;
    width: 350px;
    height: 612px;
    overflow: hidden;
    box-shadow: 0 6px 18px rgba(0,0,0,.18);
  }

  /* Front: contact side */
  .card--front { background: var(--card-dark); }
  .pattern-dark {
    position: absolute; inset: 0;
    background: radial-gradient(circle at 50% 40%, var(--card-dark) 0%, var(--card-dark-deep) 100%);
  }
  .front-content {
    position: relative;
    display: flex; flex-direction: column; align-items: center;
    padding-top: 92px;
  }
  .seal {
    width: 150px; height: 150px;
    border: 3px solid var(--gold);
    border-radius: 50%;
    display: flex; align-items: center; justify-content: center;
  }
  .seal-name {
    font-family: "Cinzel", serif;
    font-weight: 600;
    font-size: 21px;
    letter-spacing: 2px;
    color: var(--gold);
  }
  .holder-name {
    margin-top: 40px;
    font-family: "Cinzel", serif;
    font-weight: 700;
    font-size: 25px;
    letter-spacing: 1px;
    color: var(--gold);
  }
  .holder-title {
    margin-top: 6px;
    font-family: "Montserrat", sans-serif;
    font-size: 12px;
    color: var(--text-light);
  }
  .contact-list {
    list-style: none;
    margin-top: 34px;
    display: flex; flex-direction: column; align-items: center; gap: 10px;
    font-family: "Montserrat", sans-serif;
    font-size: 12px;
    color: var(--text-light);
  }
  .contact-list .bullet {
    width: 7px; height: 7px; background: var(--gold-light);
  }

  /* Back: brand side */
  .card--back { display: flex; flex-direction: column; }
  .brand-band {
    height: 176px;
    background: var(--card-dark);
    display: flex; flex-direction: column; align-items: center; justify-content: center;
  }
  .brand-country {
    font-family: "Cinzel", serif;
    font-size: 13px;
    letter-spacing: 3px;
    color: var(--gold);
  }
  .brand-rule {
    width: 230px; height: 2px; background: var(--gold);
    margin: 10px 0 12px;
  }
  .brand-name {
    font-family: "Cinzel", serif;
    font-weight: 600;
    font-size: 42px;
    letter-spacing: 3px;
    color: var(--gold);
  }
  .pattern-gold {
    position: relative;
    flex: 1;
    background: linear-gradient(135deg, var(--gold-deep) 0%, var(--gold-light) 45%, var(--gold) 70%, var(--gold-deep) 100%);
    display: flex; align-items: center; justify-content: center;
  }
  .seal--dark { border-color: var(--ink); width: 170px; height: 170px; }
  .seal--dark .seal-name { color: var(--ink); font-size: 23px; }
</style>
</head>
<body>
  <section class="card card--front">
    <div class="pattern-dark" role="img" aria-label="Fine diamond lattice pattern in dark brown"></div>
    <div class="front-content">
      <div class="seal"><span class="seal-name">VORALDI</span></div>
      <h1 class="holder-name">PAUL VORALDI</h1>
      <p class="holder-title">CEO and CO Founder</p>
      <ul class="contact-list">
        <li>555-318-4402</li>
        <li class="bullet"></li>
        <li>paul@voraldi-example.com</li>
        <li class="bullet"></li>
        <li>VORALDI.COM</li>
        <li class="bullet"></li>
        <li>4718 E Danbury</li>
      </ul>
    </div>
  </section>

  <section class="card card--back">
    <header class="brand-band">
      <span class="brand-country">ITALY</span>
      <span class="brand-rule"></span>
      <span class="brand-name">VORALDI</span>
    </header>
    <div class="pattern-gold" role="img" aria-label="Gold diamond lattice pattern behind the brand seal">
      <div class="seal seal--dark"><span class="seal-name">VORALDI</span></div>
    </div>
  </section>
</body>
</html>
```